Logo & Visitenkarte für selbständige Lerntherapeutin
Ich bin sehr zufrieden mit seiner Arbeitsweise und dem Ergebnis. Das Logo und die Visitenkarte entsprechen genau meinen Vorstellungen. Schnell hat er jeweils auf meine Veränderungswünsche reagiert und sehr kreative Ideen eingebracht. Herzlichen Dank!
Zielgruppe
Ich bin selbständige Lerntherapeutin in meiner eigenen Praxis und unterstütze Lernende in ihrem Lernprozess. Das Logo soll Lernende (Schüler ab ca. 10 Jahren, Lehrlinge, Studierende) sowie ihre Eltern ansprechen, da ich auch eng mit diesen arbeite.
I am an independent learning therapist in my own practice and support learners in their learning process. The logo is intended to appeal to learners (students over the age of 10, apprentices, students) and their parents, as I also work closely with them.
Aufgabenstellung
Für mich sind die Themen Motivation, Freude, Mut, Selbstvertrauen, Lernerfolg und persönliche Entwicklung zentrale Themen bei der Arbeit.
Logos wenn möglich auch in SVG Format.
For me, the topics of motivation, joy, courage, self-confidence, learning success and personal development are key topics at work.
Logos also in SVG format if possible.

```html
<!DOCTYPE html>
<html lang="de">
<head>
<meta charset="utf-8">
<title>Visitenkarte – Merkwerk</title>
<link rel="stylesheet" href="https://fonts.googleapis.com/css2?family=Didact+Gothic&display=swap">
<style>
  :root {
    --page-bg: #ececec;
    --card-bg: #ffffff;
    --brand-red: #e30613;
    --text-grey: #6b6b6b;
  }
  html, body {
    margin: 0;
    width: 1200px;
    height: 1200px;
    overflow: hidden;
    background: var(--page-bg);
    font-family: "Didact Gothic", sans-serif;
  }
  .business-card {
    position: absolute;
    left: 50px;
    top: 232px;
    width: 1100px;
    height: 736px;
    background: var(--card-bg);
    color: var(--text-grey);
    text-align: center;
  }
  .brand-name {
    position: absolute;
    top: 84px;
    left: 0;
    right: 0;
    margin: 0;
    font-size: 118px;
    line-height: 1;
    font-weight: normal;
    color: var(--brand-red);
    letter-spacing: 1px;
  }
  .person-name {
    position: absolute;
    left: 0; right: 0;
    top: 304px;
    margin: 0;
    font-size: 47px;
    line-height: 1.2;
    font-weight: normal;
  }
  .person-role {
    position: absolute;
    left: 0; right: 0;
    top: 370px;
    margin: 0;
    font-size: 29px;
    line-height: 1.2;
  }
  .address, .contact {
    position: absolute;
    left: 0; right: 0;
    margin: 0;
    font-size: 28px;
    line-height: 34px;
    font-style: normal;
  }
  .address { top: 456px; }
  .contact { top: 548px; }
  .contact .label { margin-right: 12px; }
</style>
</head>
<body>
  <article class="business-card">
    <p class="brand-name">Merkwerk</p>
    <h1 class="person-name">Vorname Nachname</h1>
    <p class="person-role">selbständige Lerntherapeutin</p>
    <address class="address">
      Musterstraße 12<br>
      12345 Musterstadt
    </address>
    <p class="contact">
      <span class="label">Telefon:</span>+49 (0) 123 - 45 67 8910<br>
      <span class="label">E-Mail:</span>muster@email.de<br>
      <span class="label">Internet:</span>www.muster.de
    </p>
  </article>
</body>
</html>
```